Need Bold, Hip Card for Concert Ticket Website Gleaming Passes!

Hi there! I am putting together a business/website that sells event tickets (mostly concerts, but also some sports and theater). Think SeatNook, but much smaller. The site is called Gleaming Passes. I have a new logo (attached, with black/red/white color scheme), and am looking for a modern/cool/original business card design. Note that I am thinking of having the card itself in the shape of a ticket (die cut), so you may want to keep that in mind when designing, but I'm not set on that. I'm also open to alternative card sizes, thicknesses, glossy, spot UV, etc. in order to stand out. I'm attaching a potential die cut template and a sample card using that template in case you want to work with that.
Target Market(s)
Music fans, people that like going to see live events
Industry/Entity Type
Entertainment
Contact Information for Business Card
Information that I'd like to have:
website address - www.gleamingpasses.example
phone number: 1-833-5GLEAMNG (532-6264)
my name - Wendel Pike

```html
<!DOCTYPE html>
<html lang="en">
<head>
<meta charset="utf-8">
<title>Gleaming Passes – Business Card</title>
<link href="https://fonts.googleapis.com/css2?family=Montserrat:wght@700;800&family=Open+Sans:wght@400;600&display=swap" rel="stylesheet">
<style>
  :root {
    --red: #e8202a;
    --ink: #1c1b1f;
    --dark-1: #2a2930;
    --dark-2: #131216;
    --paper: #ffffff;
    --stage: #ecebe8;
    --text: #3a3a3e;
  }
  * { box-sizing: border-box; margin: 0; padding: 0; }
  html, body { width: 1200px; height: 891px; overflow: hidden; }
  body {
    background: var(--stage);
    font-family: "Open Sans", Arial, sans-serif;
    position: relative;
  }
  .card {
    position: absolute;
    width: 540px;
    height: 309px;
    background: var(--paper);
    overflow: hidden;
    box-shadow: 0 10px 28px rgba(0,0,0,.18);
  }
  .card--front { left: 40px; top: 291px; }
  .card--back  { left: 620px; top: 291px; }

  /* brand name */
  .brand {
    display: flex;
    align-items: center;
    gap: 10px;
  }
  .brand__mark {
    width: 16px; height: 16px;
    background: var(--red);
  }
  .brand__name {
    font-family: "Montserrat", Arial, sans-serif;
    font-weight: 800;
    text-transform: uppercase;
    letter-spacing: 2px;
    white-space: nowrap;
  }

  /* back side */
  .back__brand {
    position: absolute;
    left: 0; right: 0; top: 118px;
    justify-content: center;
  }
  .back__brand .brand__name { color: var(--ink); font-size: 26px; }
  .back__url {
    position: absolute;
    left: 0; right: 0; top: 222px;
    text-align: center;
    font-family: "Montserrat", Arial, sans-serif;
    font-weight: 700;
    font-size: 10px;
    letter-spacing: 5px;
    color: var(--ink);
    white-space: nowrap;
  }

  /* front side */
  .front__photo {
    position: absolute;
    left: 0; top: 0;
    width: 540px; height: 175px;
    background: linear-gradient(180deg, var(--dark-1) 0%, var(--dark-2) 100%);
    clip-path: polygon(0 0, 100% 0, 100% 100%, 0 86%);
  }
  .front__brand {
    position: absolute;
    left: 0; right: 0; top: 62px;
    justify-content: center;
  }
  .front__brand .brand__name { color: var(--paper); font-size: 24px; }
  .front__address-band {
    position: absolute;
    left: 160px; top: 158px;
    width: 380px; height: 30px;
    background: var(--red);
    clip-path: polygon(0 0, 100% 0, 100% 100%, 8% 100%);
    color: var(--paper);
    font-size: 11px;
    font-weight: 600;
    display: flex;
    align-items: center;
    padding-left: 60px;
    white-space: nowrap;
  }
  .front__url-band {
    position: absolute;
    left: 0; bottom: 0;
    width: 320px; height: 34px;
    background: var(--red);
    clip-path: polygon(0 0, 90% 0, 100% 100%, 0 100%);
    color: var(--paper);
    font-size: 10px;
    letter-spacing: 3px;
    display: flex;
    align-items: center;
    padding-left: 24px;
    white-space: nowrap;
  }
  .front__person {
    position: absolute;
    left: 40px; top: 204px;
  }
  .person__name {
    font-size: 22px;
    color: var(--text);
    font-weight: 400;
    white-space: nowrap;
  }
  .person__role {
    font-size: 11px;
    color: var(--red);
    margin-top: 2px;
  }
  .front__divider {
    position: absolute;
    left: 276px; top: 210px;
    width: 1.5px; height: 56px;
    background: var(--red);
  }
  .front__contacts {
    position: absolute;
    left: 300px; top: 206px;
    list-style: none;
    display: flex;
    flex-direction: column;
    gap: 6px;
  }
  .contact {
    display: flex;
    align-items: center;
    gap: 8px;
    font-size: 11px;
    color: var(--text);
    white-space: nowrap;
  }
  .contact__icon {
    width: 16px; height: 16px;
    flex: none;
  }
</style>
</head>
<body>

  <section class="card card--front" aria-label="Business card front">
    <div class="front__photo" role="img" aria-label="Dark photo of a concert crowd in front of a stage"></div>
    <div class="brand front__brand">
      <span class="brand__mark"></span>
      <span class="brand__name">Gleaming Passes</span>
    </div>
    <div class="front__address-band">Your Company Address 9912-B</div>

    <div class="front__person">
      <p class="person__name">Wendel Pike</p>
      <p class="person__role">Entertainment</p>
    </div>

    <div class="front__divider"></div>

    <ul class="front__contacts">
      <li class="contact">
        <svg class="contact__icon" viewBox="0 0 16 16" aria-hidden="true">
          <circle cx="8" cy="8" r="8" fill="#e8202a"/>
          <path d="M5.2 4.5l1.5-.3.8 2-1 .7a5 5 0 0 0 2.6 2.6l.7-1 2 .8-.3 1.5c-3.6.3-6.6-2.7-6.3-6.3z" fill="#fff"/>
        </svg>
        1-833-5GLEAMNG (532-6264)
      </li>
      <li class="contact">
        <svg class="contact__icon" viewBox="0 0 16 16" aria-hidden="true">
          <circle cx="8" cy="8" r="8" fill="#e8202a"/>
          <rect x="4" y="5" width="8" height="6" fill="#fff"/>
          <path d="M4 5l4 3.2L12 5" fill="none" stroke="#e8202a" stroke-width="1"/>
        </svg>
        hello@gleamingpasses.example
      </li>
      <li class="contact">
        <svg class="contact__icon" viewBox="0 0 16 16" aria-hidden="true">
          <circle cx="8" cy="8" r="8" fill="#e8202a"/>
          <rect x="4" y="4.5" width="8" height="5.5" fill="none" stroke="#fff" stroke-width="1.2"/>
          <path d="M6 12h4M8 10v2" stroke="#fff" stroke-width="1.2"/>
        </svg>
        www.gleamingpasses.example
      </li>
    </ul>

    <div class="front__url-band">www.gleamingpasses.example</div>
  </section>

  <section class="card card--back" aria-label="Business card back">
    <div class="brand back__brand">
      <span class="brand__mark"></span>
      <span class="brand__name">Gleaming Passes</span>
    </div>
    <p class="back__url">www.gleamingpasses.example</p>
  </section>

</body>
</html>
```